Accounting company website and Facebook page design

I need a website designed and copy written for an accounting/bookkeeping company in Ohio. We have content but would need someone to fine-tune it and make it sound good. I also need a Facebook page design created. Attached is the logo for the company.

```html
<!DOCTYPE html>
<html lang="en">
<head>
<meta charset="utf-8">
<title>The Steadfast Group, Inc. — Accounting, Bookkeeping &amp; Tax Prep</title>
<link href="https://fonts.googleapis.com/css2?family=Cinzel:wght@400;600&family=Poppins:wght@300;400;500&display=swap" rel="stylesheet">
<style>
:root{
  --gold:#eba31a;
  --gold-soft:#f7e0a6;
  --dark:#232326;
  --dark-2:#2c2c30;
  --cream:#fdf9ef;
  --ink:#2a2a2a;
  --body:#555;
  --white:#fff;
}
*{box-sizing:border-box;margin:0;padding:0}
html,body{width:1200px;height:2884px;overflow:hidden}
body{position:relative;font-family:"Poppins",sans-serif;color:var(--body);background:var(--white)}
.abs{position:absolute}
.serif{font-family:"Cinzel",serif}
.btn{position:absolute;display:flex;align-items:center;justify-content:center;background:var(--gold);color:var(--white);font-size:14px;font-weight:400;height:38px}
.btn::after{content:"";position:absolute;right:-12px;top:0;width:2px;height:100%;background:var(--gold);transform:skewX(28deg);transform-origin:bottom}
.btn.light{background:var(--white);color:var(--ink)}
.btn.light::after{background:var(--white)}

/* hero */
.hero{position:absolute;left:0;top:0;width:1200px;height:638px;background:linear-gradient(100deg,#1c1c1f,#2e2e32 60%,#242427);overflow:hidden}
.brand{position:absolute;left:60px;top:30px;font-family:"Cinzel",serif;color:var(--gold);font-size:20px;line-height:1.05;letter-spacing:1px;display:flex;align-items:center;gap:10px}
.brand .dot{width:12px;height:12px;background:var(--gold);border-radius:50%}
.nav{position:absolute;top:36px;left:402px;display:flex;gap:0;font-size:14px;color:var(--white)}
.nav a{color:inherit;text-decoration:none;position:absolute;white-space:nowrap}
.nav a.active{color:var(--gold)}
.hero-photo{position:absolute;left:720px;top:110px;width:400px;height:528px;background:radial-gradient(ellipse at 50% 35%,#5a4a42,#2a2626 70%)}
.hero-title{position:absolute;left:63px;top:166px;font-family:"Cinzel",serif;font-size:58px;line-height:64px;color:var(--white);letter-spacing:2px}
.hero-title .g{color:var(--gold)}
.hero-sub{position:absolute;left:62px;top:374px;color:var(--white);font-size:14px}
.scroll{position:absolute;left:48px;top:530px;transform-origin:left top;transform:rotate(-90deg) translateX(-100px);color:var(--white);font-size:11px;letter-spacing:3px;width:100px}

/* welcome */
.section-title{position:absolute;left:0;width:1200px;text-align:center;font-family:"Cinzel",serif;font-size:29px;color:var(--ink);letter-spacing:1px}
.section-title .g{color:var(--gold)}
.rule{position:absolute;height:1px;background:var(--gold)}
.welcome-text{position:absolute;left:286px;top:812px;width:628px;text-align:center;font-size:14px;line-height:22.5px;color:var(--body)}

/* services */
.services{position:absolute;left:0;top:1137px;width:1200px;height:431px;background:var(--cream)}
.svc{position:absolute;width:278px;height:278px;border-radius:50%;background:var(--gold-soft);text-align:center;color:var(--body)}
.svc h3{font-family:"Cinzel",serif;font-weight:400;font-size:17px;color:var(--gold);margin-top:100px;letter-spacing:1px}
.svc p{font-size:14px;line-height:22.5px;width:240px;margin:8px auto 0}
.svc .more{font-size:13px;color:var(--gold);margin-top:11px;display:block}
.svc svg.icon{position:absolute;left:111px;top:32px}
.svc.feature{background:var(--gold);color:var(--white);box-shadow:0 0 0 5px var(--gold),0 0 0 8px var(--dark)}
.svc.feature h3,.svc.feature .more{color:var(--white)}

/* news */
.news-img{position:absolute;width:262px;height:267px}
.news-body{position:absolute;width:230px}
.meta{display:flex;align-items:center;gap:8px;font-size:13px;color:var(--body)}
.meta svg{flex:none}
.news-body h4{font-family:"Cinzel",serif;font-weight:400;font-size:17px;line-height:24px;color:var(--ink);margin-top:12px;letter-spacing:.5px}
.news-body p{font-size:14px;line-height:22.5px;margin-top:6px}
.news-body .more{display:block;color:var(--gold);font-size:14px;margin-top:14px}

/* contact */
.contact-photo{position:absolute;left:0;top:2116px;width:600px;height:469px;background:linear-gradient(120deg,#e9ecef,#b9c7d8 45%,#6d88b0 70%,#d8d6d0)}
.contact-panel{position:absolute;left:600px;top:2116px;width:600px;height:469px;background:var(--gold)}
.field{position:absolute;left:676px;width:414px;height:34px;background:var(--white);font-size:13px;color:var(--ink);padding:8px 14px}

/* footer */
.footer{position:absolute;left:0;top:2585px;width:1200px;height:262px;background:var(--dark)}
.f-head{position:absolute;top:2638px;font-family:"Cinzel",serif;font-size:15px;color:var(--gold)}
.f-list{position:absolute;left:338px;list-style:none;font-size:13px;color:var(--white)}
.f-list li{position:absolute;white-space:nowrap}
.f-list li::before{content:"";position:absolute;left:-20px;top:7px;width:5px;height:5px;border-radius:50%;background:var(--gold)}
.f-contact{position:absolute;left:612px;display:flex;align-items:center;gap:10px;font-size:13px;color:var(--white)}
.copyright{position:absolute;left:0;top:2847px;width:1200px;height:37px;background:var(--gold);color:var(--white);font-size:13px;text-align:center;line-height:37px}
</style>
</head>
<body>

<header class="hero">
  <div class="hero-photo" role="img" aria-label="Photo of a businesswoman in a dark blazer holding blue folders"></div>
  <svg class="abs" style="left:0;top:0" width="1200" height="638" aria-hidden="true">
    <polyline points="571,638 650,535 728,547 1064,193 1165,241 1200,190" fill="none" stroke="#eba31a" stroke-width="1.6"/>
    <g fill="#eba31a"><circle cx="650" cy="535" r="3.5"/><circle cx="1064" cy="193" r="3.5"/><circle cx="1165" cy="241" r="3.5"/></g>
  </svg>
  <div class="brand"><span class="dot"></span>THE STEADFAST<br>GROUP, INC.</div>
  <nav class="nav">
    <a class="active" style="left:0">Home</a>
    <a style="left:83px">About</a>
    <a style="left:166px">Services</a>
    <a style="left:263px">News</a>
    <a style="left:343px">Contact</a>
  </nav>
  <div class="btn" style="left:1008px;top:26px;width:118px">Get A Quote</div>
  <h1 class="hero-title" style="font-weight:400">BUSINESS<br><span class="g">ACCOUNTING</span><br><span class="g">&amp; TAX</span> SERVICES</h1>
  <p class="hero-sub">Just A Click Away...</p>
  <div class="btn" style="left:59px;top:452px;width:115px">Get Started</div>
  <div class="scroll">SCROLL DOWN</div>
</header>
<svg class="abs" style="left:54px;top:638px" width="14" height="76" aria-hidden="true">
  <line x1="6" y1="0" x2="6" y2="72" stroke="#eba31a" stroke-width="1.4"/>
  <polyline points="1,66 6,73 11,66" fill="none" stroke="#eba31a" stroke-width="1.4"/>
</svg>

<section class="welcome">
  <div class="rule" style="left:498px;top:757px;width:204px"></div>
  <h2 class="section-title" style="top:770px;font-weight:400">WELCOME TO <span class="g">ACCOUNTING THE STEADFAST GROUP</span></h2>
  <p class="welcome-text">Lorem Ipsum is simply dummy text of the printing and typesetting industry. Lorem Ipsum has been the industry's standard dummy text ever since the 1500s, when an unknown printer took a galley of type and scrambled it to make a type specimen book. It has survived not only five centuries, but also the leap into electronic typesetting, remaining essentially unchanged. It was popularised in the 1960s with the release of Letraset sheets containing Lorem Ipsum passages, and more recently with desktop publishing software like Aldus PageMaker including versions of Lorem Ipsum.</p>
  <div class="btn" style="left:533px;top:1016px;width:116px">Learn More</div>
</section>

<section class="services">
  <div class="rule" style="left:420px;top:63px;width:62px"></div>
  <div class="rule" style="left:718px;top:63px;width:62px"></div>
  <h2 class="section-title" style="top:43px;font-weight:400">OUR <span class="g">SERVICES</span></h2>

  <div class="svc" style="left:150px;top:99px">
    <svg class="icon" width="56" height="56" viewBox="0 0 56 56" fill="none" stroke="#3a3a3a" stroke-width="2" aria-hidden="true">
      <rect x="6" y="4" width="22" height="30" rx="2" stroke="#eba31a"/>
      <rect x="20" y="12" width="24" height="34" rx="2"/>
      <line x1="25" y1="20" x2="39" y2="20"/><line x1="25" y1="26" x2="39" y2="26"/><line x1="25" y1="32" x2="35" y2="32"/>
      <circle cx="22" cy="44" r="8" stroke="#eba31a"/><line x1="48" y1="26" x2="36" y2="48"/>
    </svg>
    <h3>ACCOUNTING</h3>
    <p>Lorem Ipsum is simply dummy text of the printing and typesetting industry. Lorem Ipsum.</p>
    <span class="more">Read More ⟶</span>
  </div>

  <div class="svc feature" style="left:461px;top:99px">
    <svg class="icon" width="56" height="56" viewBox="0 0 56 56" fill="none" stroke="#fff" stroke-width="2" aria-hidden="true">
      <rect x="6" y="4" width="22" height="46" rx="3"/>
      <rect x="24" y="14" width="26" height="36" rx="3"/>
      <rect x="29" y="19" width="16" height="7"/>
      <line x1="30" y1="32" x2="44" y2="32"/><line x1="30" y1="38" x2="44" y2="38"/><line x1="30" y1="44" x2="44" y2="44"/>
      <line x1="11" y1="12" x2="20" y2="12"/><line x1="11" y1="18" x2="20" y2="18"/>
    </svg>
    <h3>BOOKKEEPING</h3>
    <p>Lorem Ipsum is simply dummy text of the printing and typesetting industry. Lorem Ipsum.</p>
    <span class="more">Read More ⟶</span>
  </div>

  <div class="svc" style="left:774px;top:99px">
    <svg class="icon" width="56" height="56" viewBox="0 0 56 56" fill="none" stroke="#3a3a3a" stroke-width="2" aria-hidden="true">
      <path d="M8 4h26l8 8v40H8z"/>
      <circle cx="22" cy="18" r="7" stroke="#eba31a"/>
      <line x1="14" y1="32" x2="34" y2="32"/><line x1="14" y1="38" x2="30" y2="38"/><line x1="14" y1="44" x2="24" y2="44"/>
      <line x1="50" y1="22" x2="32" y2="48" stroke="#eba31a"/>
    </svg>
    <h3>TAX PREP</h3>
    <p>Lorem Ipsum is simply dummy text of the printing and typesetting industry. Lorem Ipsum.</p>
    <span class="more">Read More ⟶</span>
  </div>
</section>

<section class="news">
  <div class="rule" style="left:387px;top:1662px;width:62px"></div>
  <div class="rule" style="left:751px;top:1662px;width:62px"></div>
  <h2 class="section-title" style="top:1642px;font-weight:400">OUR <span class="g">LATEST NEWS</span></h2>

  <div class="news-img" style="left:60px;top:1699px;background:linear-gradient(135deg,#6b4a33,#3b3b3b 50%,#bdbdbd)" role="img" aria-label="Photo of a calculator and colourful binders on a wooden desk"></div>
  <div class="news-body" style="left:346px;top:1742px">
    <div class="meta">
      <svg width="16" height="16" viewBox="0 0 16 16" fill="none" stroke="#eba31a" stroke-width="1.3"><rect x="1.5" y="3" width="13" height="11.5" rx="1"/><line x1="1.5" y1="6.5" x2="14.5" y2="6.5"/><line x1="5" y1="1" x2="5" y2="4"/><line x1="11" y1="1" x2="11" y2="4"/></svg>
      <span>15, Aug 2022</span>
      <svg style="margin-left:16px" width="20" height="16" viewBox="0 0 20 16" fill="none" stroke="#eba31a" stroke-width="1.3"><path d="M3 3h14v8H8l-4 3v-3H3z"/></svg>
      <span style="margin-left:14px">155</span>
    </div>
    <h4>LOREM IPSUM IS SIMPLY DUMMY TEXT.</h4>
    <p>Lorem Ipsum is simply dummy text of the printing and typesetting industry.</p>
    <span class="more">Read More</span>
  </div>

  <div class="news-img" style="left:615px;top:1699px;background:linear-gradient(135deg,#dcdcdc,#c7bfb5 50%,#9a9a9a)" role="img" aria-label="Photo of hands using a calculator beside cash and a card"></div>
  <div class="news-body" style="left:900px;top:1742px">
    <div class="meta">
      <svg width="16" height="16" viewBox="0 0 16 16" fill="none" stroke="#eba31a" stroke-width="1.3"><rect x="1.5" y="3" width="13" height="11.5" rx="1"/><line x1="1.5" y1="6.5" x2="14.5" y2="6.5"/><line x1="5" y1="1" x2="5" y2="4"/><line x1="11" y1="1" x2="11" y2="4"/></svg>
      <span>15, Aug 2022</span>
      <svg style="margin-left:16px" width="20" height="16" viewBox="0 0 20 16" fill="none" stroke="#eba31a" stroke-width="1.3"><path d="M3 3h14v8H8l-4 3v-3H3z"/></svg>
      <span style="margin-left:14px">155</span>
    </div>
    <h4>LOREM IPSUM IS SIMPLY DUMMY TEXT.</h4>
    <p>Lorem Ipsum is simply dummy text of the printing and typesetting industry.</p>
    <span class="more">Read More</span>
  </div>

  <div class="btn" style="left:539px;top:2009px;width:108px">View More</div>
</section>

<section class="contact">
  <div class="contact-photo" role="img" aria-label="Photo of a smiling support agent with a headset working at a laptop"></div>
  <div class="contact-panel"></div>
  <h2 class="abs serif" style="left:675px;top:2153px;font-size:29px;font-weight:400;color:var(--white);letter-spacing:2px">GET IN TOUCH</h2>
  <div class="rule" style="left:914px;top:2172px;width:62px;background:var(--white)"></div>
  <div class="field" style="top:2210px">Name*</div>
  <div class="field" style="top:2256px">E-mail*</div>
  <div class="field" style="top:2303px">Phone No.*</div>
  <div class="field" style="top:2349px;height:130px;padding-left:18px">Massage*</div>
  <div class="btn light" style="left:676px;top:2502px;width:88px">Submit</div>
</section>

<footer class="footer"></footer>
<div class="abs serif" style="left:60px;top:2655px;color:var(--white);font-size:30px;line-height:34px;letter-spacing:1px">THE STEADFAST<br>GROUP, INC.</div>
<div class="abs" style="left:60px;top:2740px;color:var(--white);font-size:9.5px;letter-spacing:1px">ACCOUNTING, BOOKKEEPING AND TAX PREP</div>

<div class="f-head" style="left:338px">QUICK LINKS</div>
<ul class="f-list" style="top:2669px">
  <li style="left:23px;top:0">Home</li>
  <li style="left:23px;top:28px">About Us</li>
  <li style="left:23px;top:55px">Services</li>
  <li style="left:23px;top:83px">News</li>
  <li style="left:23px;top:112px">Contact Us</li>
</ul>

<div class="f-head" style="left:614px">CONTACT US</div>
<div class="f-contact" style="top:2670px">
  <svg width="16" height="18" viewBox="0 0 16 18" fill="none" stroke="#eba31a" stroke-width="1.3"><path d="M8 17s6-6 6-10A6 6 0 0 0 2 7c0 4 6 10 6 10z"/><circle cx="8" cy="7" r="2.2"/></svg>
  <span>123 , Lorem ipsum is a dummy text.</span>
</div>
<div class="f-contact" style="top:2709px">
  <svg width="18" height="18" viewBox="0 0 18 18" fill="none" stroke="#eba31a" stroke-width="1.3"><path d="M4 2l3 3-2 2c1 2 3 4 5 5l2-2 3 3-2 2C8 15 3 10 2 4z"/></svg>
  <span style="font-weight:500">123 456 7890</span>
</div>
<div class="f-contact" style="top:2747px">
  <svg width="20" height="16" viewBox="0 0 20 16" fill="none" stroke="#eba31a" stroke-width="1.3"><rect x="1" y="2" width="18" height="12"/><polyline points="1,2 10,9 19,2"/></svg>
  <span>info@steadfastgroup.example</span>
</div>

<div class="f-head" style="left:890px">SUBSCRIBE TO OUR NEWSLATTER</div>
<div class="abs" style="left:890px;top:2672px;width:250px;height:33px;background:var(--white);border-radius:17px;font-size:12px;color:var(--ink);padding:8px 15px">E-mail*</div>
<div class="abs" style="left:890px;top:2722px;width:88px;height:33px;background:var(--gold);border-radius:17px;color:var(--white);font-size:12px;text-align:center;line-height:33px">Subscribe</div>

<div class="copyright">Copyright © 2022 <strong style="font-weight:500">THE STEADFAST GROUP INC.</strong> All rights reserved.</div>

</body>
</html>
```